Dane Morrow Photography Business Card

I am looking for a simple, yet elegant business card for my photography business.

It is a short turn around project as the cards need to be printed within 48 hours. So the earlier you submit, the more likely you are to be chosen.

I am a professional portrait, sports and commercial photographer located in Brisbane, Australia. I am looking for a professional business card to distribute to professional clients. The card needs to be professional and easy to read. It must have my contact information as listed below.

Industry/Entity Type

Business

Contact Information for Business Card

Dane Morrow Photography
www.danemorrowphoto.com.au
dane@danemorrowphoto.com.au
+61 437 280 556

Font styles to use
Serif
Sans Serif

Colors
ffc214
fece3e
fee18a

Requirements
Must have
• Must have contact information as above,
• Please use a similar colourscheme to the one provided in the logo upload.
Nice to have
• A very simple, design, happy to have some geometric shapes etc. Must look professional

```html
<!DOCTYPE html>
<html lang="en">
<head>
<meta charset="utf-8">
<title>Dane Morrow Photography — Business Card</title>
<link rel="stylesheet" href="https://fonts.googleapis.com/css2?family=Mulish:wght@300;400&family=Arimo&display=swap">
<style>
  :root {
    --page: #ffffff;
    --card-light: #ffffff;
    --card-dark: #0c0d0f;
    --edge: #3d4a48;
    --wordmark: #4a4b50;
    --gold: #e0a02e;
    --contact: #ffffff;
  }
  * { margin: 0; padding: 0; box-sizing: border-box; }
  html, body { width: 1200px; height: 1200px; overflow: hidden; background: var(--page); }
  .canvas { position: relative; width: 1200px; height: 1200px; }

  .card {
    position: absolute;
    width: 838px;
    height: 478px;
    border-radius: 40px;
    border: 1px solid var(--edge);
    background: var(--card-light);
    overflow: hidden;
  }
  .card--front { left: 184px; top: 106px; }
  .card--back  { left: 177px; top: 614px; }

  .card__dark-panel {
    position: absolute;
    left: 305px; top: 0; right: 0; bottom: 0;
    background: var(--card-dark);
  }

  .brand-mark {
    position: absolute;
    left: 135px;
    width: 150px;
    text-align: center;
    font-family: "Mulish", sans-serif;
    font-weight: 400;
    font-size: 26px;
    line-height: 1.15;
    letter-spacing: 1px;
    text-transform: uppercase;
    color: var(--gold);
  }
  .card--front .brand-mark { top: 208px; }
  .card--back  .brand-mark { top: 146px; }

  .wordmark {
    position: absolute;
    left: 318px;
    font-family: "Mulish", sans-serif;
    font-weight: 300;
    color: var(--wordmark);
    text-transform: uppercase;
    white-space: nowrap;
  }
  .wordmark__name {
    display: block;
    font-size: 62px;
    line-height: 1;
    letter-spacing: -2.5px;
  }
  .wordmark__trade {
    display: block;
    font-size: 34px;
    line-height: 1;
    letter-spacing: -1.2px;
    margin-top: 2px;
  }
  .card--front .wordmark { top: 192px; }
  .card--back  .wordmark { top: 134px; }

  .contact-list {
    position: absolute;
    left: 262px;
    top: 322px;
    list-style: none;
  }
  .contact-list__item {
    display: flex;
    align-items: center;
    height: 36px;
  }
  .contact-list__icon {
    width: 24px; height: 24px;
    margin-right: 40px;
    flex: none;
  }
  .contact-list__text {
    font-family: "Arimo", sans-serif;
    font-size: 24px;
    color: var(--contact);
    white-space: nowrap;
  }
</style>
</head>
<body>
<main class="canvas">

  <section class="card card--front" aria-label="Business card front">
    <div class="card__dark-panel"></div>
    <div class="brand-mark">Dane<br>Morrow</div>
    <h1 class="wordmark">
      <span class="wordmark__name">Dane Morrow</span>
      <span class="wordmark__trade">Photography</span>
    </h1>
  </section>

  <section class="card card--back" aria-label="Business card back">
    <div class="card__dark-panel"></div>
    <div class="brand-mark">Dane<br>Morrow</div>
    <h2 class="wordmark">
      <span class="wordmark__name">Dane Morrow</span>
      <span class="wordmark__trade">Photography</span>
    </h2>
    <ul class="contact-list">
      <li class="contact-list__item">
        <svg class="contact-list__icon" viewBox="0 0 24 24" aria-hidden="true">
          <rect x="6" y="1.5" width="12" height="21" rx="2.5" fill="none" stroke="var(--gold)" stroke-width="2"/>
          <line x1="6" y1="17" x2="18" y2="17" stroke="var(--gold)" stroke-width="1.5"/>
          <circle cx="12" cy="19.8" r="1.1" fill="var(--gold)"/>
        </svg>
        <span class="contact-list__text">+61 437 280 556</span>
      </li>
      <li class="contact-list__item">
        <svg class="contact-list__icon" viewBox="0 0 24 24" aria-hidden="true">
          <rect x="1" y="5" width="22" height="14" fill="var(--gold)"/>
          <polyline points="1.5,5.5 12,13 22.5,5.5" fill="none" stroke="#ffffff" stroke-width="1.4"/>
          <polyline points="1.5,18.5 9,11 M22.5,18.5 15,11" fill="none" stroke="#ffffff" stroke-width="1.2"/>
        </svg>
        <span class="contact-list__text">dane@danemorrowphoto.com.au</span>
      </li>
      <li class="contact-list__item">
        <svg class="contact-list__icon" viewBox="0 0 24 24" aria-hidden="true">
          <circle cx="12" cy="12" r="10" fill="none" stroke="var(--gold)" stroke-width="2"/>
          <ellipse cx="12" cy="12" rx="4.5" ry="10" fill="none" stroke="var(--gold)" stroke-width="1.6"/>
          <line x1="2" y1="12" x2="22" y2="12" stroke="var(--gold)" stroke-width="1.6"/>
          <line x1="12" y1="2" x2="12" y2="22" stroke="var(--gold)" stroke-width="1.6"/>
        </svg>
        <span class="contact-list__text">www.danemorrowphoto.com.au</span>
      </li>
    </ul>
  </section>

</main>
</body>
</html>
```